Ember Ridge Clearing postcard ( for direct mailing) and business card design

Design postcards/Business cards
Dale Horvick
Ember Ridge Clearing
482 Copperfern Rd Lewisville,NC 27023
(336) 555-0184 Dale@Emberridgeclearing.example

The postcard will be used for direct mailing to land owners and contractors to advertise our service. Pictures of the process and equipment along with a short summary of what we do. Business card should be contact info and logo.
Updates

The post cards could say something like this: Forestry Mulching machines are capable of clearing land of unwanted trees and brush with limited disturbance to soils or desirable vegetation. Traditional land clearing methods often present an increased risk of erosion by pushing over trees, uprooting the stump and roots, and substantially disturbing soils.In contrast, mulching the vegetation leaves the soil structure intact. The mulched material can be left on the ground and will act as an erosion barrier while returning nutrients back into the soil through decomposition. Over time, grass will naturally grow through the mulch and can be maintained with mowing.

Target Market(s)

Land owners and contractors who need vegetation cleared

Industry/Entity Type

Forestry Mulching

Requirements
Must have
• picture, brief description of service offered, contact info on postcard. Business card should have contact info and logo.
Nice to have
• I like contour lines as a background but I'd like to see other ideas.

```html
<!DOCTYPE html>
<html lang="en">
<head>
<meta charset="utf-8">
<title>Ember Ridge Clearing Postcard</title>
<link rel="stylesheet" href="https://fonts.googleapis.com/css2?family=Montserrat:wght@500;600;700;800&family=Oswald:wght@500;600&family=Open+Sans:wght@400&display=swap">
<style>
  :root {
    --green-dark: #136b38;
    --green-mid: #39ab4a;
    --green-lime: #8dc63f;
    --ink: #1b1b1b;
    --paper: #ffffff;
    --panel-gray: #e7e7e7;
    --stage: #d6d6d6;
  }
  * { margin: 0; padding: 0; box-sizing: border-box; }
  html, body { width: 853px; height: 1200px; overflow: hidden; background: var(--stage); }
  .card {
    position: absolute; left: 64px; width: 706px; height: 504px;
    background: var(--paper); overflow: hidden;
    font-family: "Montserrat", sans-serif; color: var(--paper);
  }
  .card-front { top: 70px; }
  .card-back { top: 618px; }
  .card-art { position: absolute; inset: 0; width: 706px; height: 504px; }
  .abs { position: absolute; white-space: nowrap; }

  .wordmark { display: flex; align-items: flex-start; gap: 8px; color: var(--ink); }
  .wordmark-square { width: 20px; height: 20px; background: var(--green-dark); margin-top: 4px; flex: none; }
  .wordmark-name { font-weight: 800; text-transform: uppercase; line-height: 0.98; }
  .front-wordmark { left: 52px; top: 40px; }
  .front-wordmark .wordmark-name { font-size: 22px; }
  .back-wordmark { left: 408px; top: 48px; }
  .back-wordmark .wordmark-name { font-size: 16px; }
  .back-wordmark .wordmark-square { width: 16px; height: 16px; }

  .headline { font-family: "Oswald", sans-serif; font-weight: 600; text-transform: uppercase; line-height: 1; }
  .tag-best { left: 46px; top: 148px; background: var(--green-lime); padding: 2px 7px 3px; font-size: 23px; }
  .title-main { left: 44px; top: 180px; color: var(--green-dark); font-size: 42px; letter-spacing: -0.3px; }
  .title-sub { left: 58px; top: 225px; font-size: 27px; }
  .title-region { left: 46px; top: 262px; color: var(--green-dark); font-size: 25px; }
  .cta { left: 46px; top: 311px; font-size: 31px; }

  .name { left: 172px; top: 388px; font-size: 18px; font-weight: 600; letter-spacing: 5px; }
  .name-last { color: var(--green-lime); }
  .phone { display: flex; align-items: center; gap: 7px; font-weight: 700; }
  .front-phone { left: 172px; top: 412px; font-size: 24px; }
  .email { left: 172px; top: 455px; font-size: 11.5px; font-weight: 500; display: flex; align-items: center; gap: 5px; }

  .company { font-weight: 700; }
  .info-line { font-weight: 500; display: flex; gap: 6px; align-items: flex-start; }
  .front-company { left: 455px; top: 376px; font-size: 18.5px; }
  .front-address { left: 437px; top: 408px; font-size: 13px; line-height: 20px; }
  .front-web { left: 437px; top: 454px; font-size: 12px; }

  .about-title { left: 72px; top: 35px; font-size: 20px; font-weight: 800; letter-spacing: 1.5px; }
  .about-copy { left: 52px; top: 81px; width: 280px; color: var(--ink); font-family: "Open Sans", sans-serif; font-size: 10.4px; line-height: 14.4px; white-space: normal; }
  .about-copy p + p { margin-top: 7px; }
  .back-phone { left: 46px; top: 311px; font-size: 25px; }
  .back-company { left: 65px; top: 376px; font-size: 19px; }
  .back-address { left: 48px; top: 406px; font-size: 13px; line-height: 20px; }
  .back-web { left: 48px; top: 452px; font-size: 12px; }

  .stamp-box { left: 594px; top: 36px; width: 71px; height: 71px; border: 1px solid var(--ink); }
  .address-rule { left: 482px; width: 183px; height: 1px; background: var(--ink); }
</style>
</head>
<body>

<section class="card card-front">
  <svg class="card-art" viewBox="0 0 706 504">
    <defs>
      <linearGradient id="machineBig" x1="0" y1="0" x2="0" y2="1">
        <stop offset="0" stop-color="#3b3226"/>
        <stop offset="0.5" stop-color="#4d6f8c"/>
        <stop offset="0.8" stop-color="#8a4a2c"/>
        <stop offset="1" stop-color="#8f7c5e"/>
      </linearGradient>
      <linearGradient id="machineTop" x1="0" y1="0" x2="0" y2="1">
        <stop offset="0" stop-color="#9fb6cf"/>
        <stop offset="0.5" stop-color="#6f6a58"/>
        <stop offset="1" stop-color="#4f4332"/>
      </linearGradient>
      <linearGradient id="machineMid" x1="0" y1="0" x2="1" y2="1">
        <stop offset="0" stop-color="#6b5e4a"/>
        <stop offset="1" stop-color="#3a3228"/>
      </linearGradient>
      <radialGradient id="portrait" cx="0.5" cy="0.45" r="0.6">
        <stop offset="0" stop-color="#c7cdd2"/>
        <stop offset="1" stop-color="#e9ecee"/>
      </radialGradient>
    </defs>
    <rect width="706" height="504" fill="#f3f3f3"/>
    <polygon points="0,0 410,0 350,120 0,120" fill="#ffffff"/>
    <polygon points="0,0 43,0 0,119" fill="var(--green-dark)"/>
    <g role="img" aria-label="Forestry mulching machine clearing brush in a wooded lot">
      <polygon points="496,0 706,0 706,298 673,340 376,340 398,292 470,292 560,60" fill="url(#machineBig)"/>
    </g>
    <polygon points="258,166 318,16 524,22 472,168" fill="#ffffff"/>
    <g role="img" aria-label="Tracked skid steer with mulching head clearing small trees">
      <polygon points="263,163 321,19 519,25 469,164" fill="url(#machineTop)"/>
    </g>
    <polygon points="305,295 349,171 500,176 458,295" fill="#ffffff"/>
    <g role="img" aria-label="Skid steer working among bare trees">
      <polygon points="309,292 352,174 496,179 456,292" fill="url(#machineMid)"/>
    </g>
    <polygon points="46,224 330,224 317,258 46,258" fill="var(--green-lime)"/>
    <polygon points="0,307 378,307 366,348 0,348" fill="var(--green-mid)"/>
    <polygon points="0,307 30,307 16,348 0,348" fill="var(--green-dark)"/>
    <polygon points="0,372 190,349 93,504 0,504" fill="var(--green-lime)"/>
    <polygon points="424,341 673,341 706,298 706,504 393,504" fill="var(--green-mid)"/>
    <polygon points="706,410 706,504 673,504" fill="#eeeeee"/>
    <polygon points="142,364 443,364 393,504 93,504" fill="var(--green-dark)"/>
    <circle cx="97" cy="428" r="50" fill="#ffffff"/>
    <g role="img" aria-label="Portrait photo of Dale Horvick">
      <circle cx="97" cy="428" r="46" fill="url(#portrait)"/>
    </g>
  </svg>

  <div class="abs wordmark front-wordmark">
    <span class="wordmark-square"></span>
    <span class="wordmark-name">Ember<br>Ridge<br>Clearing</span>
  </div>

  <div class="abs headline tag-best">The Best</div>
  <div class="abs headline title-main">Land Clearing</div>
  <div class="abs headline title-sub">Service Provider In</div>
  <div class="abs headline title-region">North Carolina</div>
  <div class="abs headline cta">Call For Free Estimate</div>

  <div class="abs name">DALE <span class="name-last">HORVICK</span></div>
  <div class="abs phone front-phone">
    <svg width="26" height="26" viewBox="0 0 26 26" aria-hidden="true"><circle cx="13" cy="13" r="11.5" fill="none" stroke="#fff" stroke-width="2.2"/><path d="M9.3 7.5c.6-.4 1.2-.3 1.5.3l1 2c.2.5.1 1-.3 1.3l-.7.6c.5 1.5 1.6 2.7 3 3.4l.7-.6c.4-.3.9-.4 1.300-.1l1.9 1.1c.5.3.6 1 .2 1.5-.9 1.1-2.3 1.6-3.8 1-3.2-1.2-5.4-3.6-6.2-6.7-.3-1.4.3-3 1.4-3.8z" fill="#fff"/></svg>
    <span>(336) 555-0184</span>
  </div>
  <div class="abs email">
    <svg width="12" height="9" viewBox="0 0 12 9" aria-hidden="true"><rect x="0.5" y="0.5" width="11" height="8" fill="none" stroke="#8dc63f"/><path d="M0.5 0.5 6 5 11.5 0.5" fill="none" stroke="#8dc63f"/></svg>
    <span>Dale@Emberridgeclearing.example</span>
  </div>

  <div class="abs company front-company">Ember Ridge Clearing</div>
  <div class="abs info-line front-address">
    <svg width="11" height="14" viewBox="0 0 11 14" aria-hidden="true" style="margin-top:3px"><circle cx="5.5" cy="4.5" r="3.5" fill="none" stroke="#8dc63f" stroke-width="1.3"/><path d="M5.5 8v5" stroke="#8dc63f" stroke-width="1.3"/></svg>
    <span>482 Copperfern Rd Lewisville,<br>NC 27023</span>
  </div>
  <div class="abs info-line front-web">
    <svg width="12" height="12" viewBox="0 0 12 12" aria-hidden="true" style="margin-top:2px"><circle cx="6" cy="6" r="5.3" fill="none" stroke="#136b38" stroke-width="1.1"/><ellipse cx="6" cy="6" rx="2.3" ry="5.3" fill="none" stroke="#136b38" stroke-width="1"/><path d="M0.7 6h10.6" stroke="#136b38"/></svg>
    <span>www.emberridgeclearing.example</span>
  </div>
</section>

<section class="card card-back">
  <svg class="card-art" viewBox="0 0 706 504" aria-hidden="true">
    <rect width="706" height="504" fill="#ffffff"/>
    <polygon points="60,0 412,0 311,293 0,293 0,167" fill="var(--panel-gray)"/>
    <polygon points="0,0 60,0 0,167" fill="var(--green-mid)"/>
    <polygon points="28,0 60,0 0,167 0,90" fill="#2e9b3e"/>
    <polygon points="31,32 260,32 252,62 20,62" fill="var(--green-lime)"/>
    <polygon points="0,293 364,293 290,504 0,504" fill="var(--green-dark)"/>
    <polygon points="0,368 54,368 7,504 0,504" fill="var(--green-lime)"/>
    <polygon points="0,347 304,347 300,352 0,352" fill="#ffffff"/>
    <polygon points="0,306 316,306 304,347 0,347" fill="var(--green-mid)"/>
  </svg>

  <div class="abs about-title">ABOUT US</div>
  <div class="abs about-copy">
    <p>Forestry Mulching is especially economical for smaller plots of land or areas with less access. When land needs to be cleared for adding roads, servicing pipelines, or creating recreational spaces in a wooded area, forestry mulching can be a very effective method of clearing spaces.</p>
    <p>Along with making space for planned projects, forestry mulching is also a great way to clear unwanted vegetation to allow more desirable food sources for local wildlife to flourish. Creating access to waterways that have become overgrown and clearing space for animals to gain new breeding grounds are other ways forestry mulching can be helpful.</p>
  </div>

  <div class="abs phone back-phone">
    <svg width="27" height="27" viewBox="0 0 26 26" aria-hidden="true"><circle cx="13" cy="13" r="11.5" fill="none" stroke="#fff" stroke-width="2.2"/><path d="M9.3 7.5c.6-.4 1.2-.3 1.5.3l1 2c.2.5.1 1-.3 1.3l-.7.6c.5 1.5 1.6 2.7 3 3.4l.7-.6c.4-.3.9-.4 1.3-.1l1.9 1.1c.5.3.6 1 .2 1.5-.9 1.1-2.3 1.6-3.8 1-3.2-1.2-5.4-3.6-6.2-6.7-.3-1.4.3-3 1.4-3.8z" fill="#fff"/></svg>
    <span>(336) 555-0184</span>
  </div>

  <div class="abs company back-company">Ember Ridge Clearing</div>
  <div class="abs info-line back-address">
    <svg width="11" height="14" viewBox="0 0 11 14" aria-hidden="true" style="margin-top:3px"><circle cx="5.5" cy="4.5" r="3.5" fill="none" stroke="#8dc63f" stroke-width="1.3"/><path d="M5.5 8v5" stroke="#8dc63f" stroke-width="1.3"/></svg>
    <span>482 Copperfern Rd Lewisville,<br>NC 27023</span>
  </div>
  <div class="abs info-line back-web">
    <svg width="12" height="12" viewBox="0 0 12 12" aria-hidden="true" style="margin-top:2px"><circle cx="6" cy="6" r="5.3" fill="none" stroke="#39ab4a" stroke-width="1.1"/><ellipse cx="6" cy="6" rx="2.3" ry="5.3" fill="none" stroke="#39ab4a" stroke-width="1"/><path d="M0.7 6h10.6" stroke="#39ab4a"/></svg>
    <span>www.emberridgeclearing.example</span>
  </div>

  <div class="abs wordmark back-wordmark">
    <span class="wordmark-square"></span>
    <span class="wordmark-name">Ember<br>Ridge<br>Clearing</span>
  </div>
  <div class="abs stamp-box"></div>
  <div class="abs address-rule" style="top:280px"></div>
  <div class="abs address-rule" style="top:321px"></div>
  <div class="abs address-rule" style="top:362px"></div>
</section>

</body>
</html>
```